Harbourline Gas and Plumbing Business Card Design

I am after a business card design for my plumbing business called 'Harbourline Gas & Plumbing'. I do all types of plumbing and gas work and specialise in general maintenance plumbing. Would like to see designs using current logo

Industry/Entity Type

Plumbing

Contact Information for Business Card

Name - Dallas McTavish
Phone number - 0468305917
Email - admin@harbourlinegasandplumbing.com.au
ABN - 58104629375

```html
<!DOCTYPE html>
<html lang="en">
<head>
<meta charset="utf-8">
<title>Harbourline Gas &amp; Plumbing – Business Card</title>
<link rel="stylesheet" href="https://fonts.googleapis.com/css2?family=Roboto:wght@400;500;700&display=swap">
<style>
  :root {
    --backdrop: #1e1e1e;
    --card-white: #ffffff;
    --brand-blue: #1d6fbd;
    --brand-navy: #2447a0;
    --brand-orange: #f07a3a;
    --brand-yellow: #fbbd22;
    --text-grey: #4a4a4a;
    --rule-grey: #777777;
  }
  * { margin: 0; padding: 0; box-sizing: border-box; }
  html, body {
    width: 1125px; height: 1200px; overflow: hidden;
    background: var(--backdrop);
    font-family: "Roboto", Arial, sans-serif;
  }
  .canvas { position: relative; width: 1125px; height: 1200px; }

  .card {
    position: absolute; left: 171px; width: 826px; height: 472px; overflow: hidden;
  }
  .card--front { top: 106px; background: var(--card-white); }
  .card--back {
    top: 639px;
    background: radial-gradient(ellipse 60% 75% at 50% 45%, var(--brand-yellow) 0%, #f6a42a 45%, var(--brand-orange) 100%);
  }

  .brand-name {
    position: absolute; right: 53px; top: 88px;
    font-weight: 700; font-size: 30px; color: var(--brand-navy);
    display: flex; align-items: center; gap: 12px;
  }
  .brand-dot { width: 16px; height: 16px; border-radius: 50%; background: var(--brand-orange); }

  .person-name {
    position: absolute; left: 53px; top: 238px;
    font-weight: 500; font-size: 31px; color: var(--brand-blue);
  }
  .divider {
    position: absolute; left: 55px; top: 296px; width: 718px; height: 2px; background: var(--rule-grey);
  }
  .contact-list { position: absolute; left: 52px; top: 318px; list-style: none; }
  .contact-item {
    display: flex; align-items: center; gap: 11px;
    font-size: 19px; color: var(--text-grey); height: 26.5px;
  }
  .contact-icon { width: 18px; height: 18px; fill: var(--brand-blue); flex: none; }
  .abn {
    position: absolute; right: 53px; top: 374px; font-size: 19px; color: var(--text-grey);
  }
  .footer-band {
    position: absolute; left: 0; bottom: 0; width: 826px; height: 44px;
    background: linear-gradient(to bottom, var(--brand-orange) 0%, var(--brand-yellow) 30%, var(--brand-blue) 62%, var(--brand-navy) 100%);
  }

  .back-name {
    position: absolute; left: 0; right: 0; top: 190px; text-align: center;
    font-weight: 700; font-size: 40px; color: #ffffff;
  }
  .back-url {
    position: absolute; left: 0; right: 0; top: 405px; text-align: center;
    font-size: 19px; letter-spacing: 0.28em; color: #ffffff;
  }
</style>
</head>
<body>
<div class="canvas">

  <section class="card card--front">
    <div class="brand-name"><span class="brand-dot"></span>Harbourline Gas &amp; Plumbing</div>

    <h1 class="person-name">Dallas McTavish</h1>
    <div class="divider"></div>

    <ul class="contact-list">
      <li class="contact-item">
        <svg class="contact-icon" viewBox="0 0 24 24"><path d="M6.6 10.8c1.4 2.8 3.8 5.1 6.6 6.6l2.2-2.2c.3-.3.7-.4 1-.2 1.1.4 2.3.6 3.6.6.6 0 1 .4 1 1V20c0 .6-.4 1-1 1C10.6 21 3 13.4 3 4c0-.6.4-1 1-1h3.5c.6 0 1 .4 1 1 0 1.3.2 2.5.6 3.6.1.3 0 .7-.2 1z"/></svg>
        0468305917
      </li>
      <li class="contact-item">
        <svg class="contact-icon" viewBox="0 0 24 24"><path d="M2 5h20v14H2z M3.5 6.5 12 12.5l8.5-6" fill="none" stroke="#1d6fbd" stroke-width="2"/><path d="M2 5h20v2l-10 6.5L2 7z"/></svg>
        admin@harbourlinegasandplumbing.com.au
      </li>
      <li class="contact-item">
        <svg class="contact-icon" viewBox="0 0 24 24"><circle cx="12" cy="12" r="10"/><path d="M2 12h20M12 2c3 3 3 17 0 20M12 2c-3 3-3 17 0 20" fill="none" stroke="#ffffff" stroke-width="1.4"/></svg>
        harbourlinegasandplumbing.com.au
      </li>
    </ul>
    <div class="abn">ABN - 58104629375</div>

    <div class="footer-band" role="img" aria-label="Decorative orange and blue band along the card's lower edge"></div>
  </section>

  <section class="card card--back">
    <div class="back-name">Harbourline Gas &amp; Plumbing</div>
    <div class="back-url">www.harbourlinegasandplumbing.com.au</div>
  </section>

</div>
</body>
</html>
```